Quarrel Ridge Advisory Business Card

Quarrel Ridge Advisory is a company that provides consulting services to the Mining Industry.

Whilst Quarrel Ridge Advisory is an Australian based company its client base is the global mining industry.

The essence of Quarrel Ridge Advisory is its a can do organisation that can make a difference to its clients by providing quality assistance and form lasting relationships.
Updates

Target Market(s)

The global Mining Industry.

Industry/Entity Type

Mining

Font styles to use
Serif

Colors

Designer to choose colors to be used in the design.

Requirements
Nice to have
• My thinking is the card would look good in black given the logo.

I would like to see written on the back side of the card " Providing Metallurgical, Management and Corporate Services to the Mining Industry"

```html
<!DOCTYPE html>
<html lang="en">
<head>
<meta charset="utf-8">
<title>Quarrel Ridge Advisory – Business Card</title>
<link href="https://fonts.googleapis.com/css2?family=Arvo:wght@400;700&family=Tinos&display=swap" rel="stylesheet">
<style>
  :root {
    --ink: #000000;
    --paper: #ffffff;
    --violet: #9900ff;
    --card-edge: #777777;
  }
  * { box-sizing: border-box; margin: 0; padding: 0; }
  html, body { width: 1200px; height: 900px; overflow: hidden; background: var(--paper); }
  .sheet {
    position: relative;
    width: 1200px;
    height: 900px;
    border: 2px solid var(--ink);
    overflow: hidden;
    font-family: "Arvo", Georgia, serif;
    color: var(--ink);
  }
  .side-label {
    position: absolute;
    left: 243px;
    font-family: "Tinos", "Times New Roman", serif;
    font-size: 31px;
    line-height: 1;
  }
  .side-label--front { top: -2px; }
  .side-label--back { top: 463px; }
  .card {
    position: absolute;
    left: 245px;
    width: 712px;
    border: 1px solid var(--card-edge);
    background: var(--paper);
    overflow: hidden;
  }
  .card--front { top: 28px; height: 407px; }
  .card--back { top: 493px; height: 420px; }
  .card__swoosh { position: absolute; left: 0; top: 0; }
  .brand {
    position: absolute;
    right: 36px;
    top: 30px;
    text-align: right;
    font-weight: 700;
    font-size: 38px;
    line-height: 46px;
    color: var(--violet);
  }
  .brand-mark {
    position: absolute;
    left: 58px;
    top: 262px;
    width: 200px;
    height: 133px;
    display: flex;
    align-items: center;
    justify-content: center;
    text-align: center;
    font-weight: 700;
    font-size: 22px;
    line-height: 1.2;
    color: var(--ink);
  }
  .contact {
    position: absolute;
    right: 36px;
    top: 256px;
    text-align: right;
    font-style: normal;
    font-size: 16.5px;
    line-height: 24.6px;
    letter-spacing: 0.3px;
  }
  .tagline {
    position: absolute;
    left: 0; right: 0;
    top: 152px;
    text-align: center;
    font-size: 23px;
    line-height: 33.5px;
  }
</style>
</head>
<body>
<div class="sheet">
  <div class="side-label side-label--front">Side 1</div>
  <section class="card card--front">
    <svg class="card__swoosh" width="140" height="407" viewBox="0 0 140 407" aria-hidden="true">
      <path d="M0 0 H134 C70 90 20 220 60 407 H0 Z" fill="var(--ink)"/>
      <path d="M0 0 H117 C58 90 14 220 60 407 H0 Z" fill="var(--violet)"/>
    </svg>
    <div class="brand">Quarrel Ridge<br>Advisory</div>
    <div class="brand-mark">Quarrel Ridge<br>Advisory</div>
    <address class="contact">
      Address : xxxxxxxxx<br>
      xxxxxxxxxxx xxxxxxx<br>
      Tel : xxxxxx xxxxxxx<br>
      Email : xxxxxxxxxx@xxxx.com<br>
      Website : www.ssssssssssssssss.com
    </address>
  </section>

  <div class="side-label side-label--back">Side 2</div>
  <section class="card card--back">
    <p class="tagline">Providing Metallurgical,<br>Management and<br>Corporate Services to the Mining Industry</p>
  </section>
</div>
</body>
</html>
```